Business Card Design

Buy and sell properties
Buy and rehab properties
Buy properties for cash
That is what I do but do need a logo
looking for some type of logo or design on it
Just started business
Back of card should say something like BUY HOUSES CASH
Overview: it is a new company. Basically I buy properties wholesale and fix them up and sell them or sell them to other fix and flippers
Background: company is new so not any background
Market: is basically anyone selling a house or buying a house. Someone that needs to sell house fast. Basically I am a cash home buyer!!!

Updates
Email on card should be:   harborlanerealtyinc@mailbox.test

Industry/Entity Type
House
Contact Information for Business Card
Harbor Lane Realty Inc
PO Box 718269
Cedar Marsh FL 32987

Dale Morrick
dmorrick@mailbox.test
555-271-6094

```html
<!DOCTYPE html>
<html lang="en">
<head>
<meta charset="UTF-8">
<title>Harbor Lane Realty Inc – Business Card</title>
<link rel="stylesheet" href="https://fonts.googleapis.com/css2?family=Ubuntu:wght@500;700&display=swap">
<style>
  :root {
    --page-bg: #ffffff;
    --page-border: #cfcfcf;
    --card-black: #050505;
    --card-sheen: #1c1c1a;
    --card-back: #0f1717;
    --swoosh-light: #e4e4e4;
    --accent-orange: #f7941e;
    --text-white: #ffffff;
    --rule-grey: #8a8f8f;
    --accent-soft: #262929;
  }
  * { margin: 0; padding: 0; box-sizing: border-box; }
  html, body {
    width: 1200px;
    height: 1000px;
    overflow: hidden;
    background: var(--page-bg);
    font-family: "Ubuntu", "Trebuchet MS", sans-serif;
  }
  .canvas {
    position: relative;
    width: 1200px;
    height: 1000px;
    border: 1px solid var(--page-border);
  }
  .card {
    position: absolute;
    top: 371px;
    width: 415px;
    height: 259px;
    border-radius: 12px;
    overflow: hidden;
  }
  .card-front {
    left: 160px;
    background: linear-gradient(90deg, var(--card-black) 0%, var(--card-black) 45%, var(--card-sheen) 75%, var(--card-black) 100%);
  }
  .card-back {
    left: 626px;
    background: var(--card-back);
  }
  .card-art {
    position: absolute;
    inset: 0;
    width: 100%;
    height: 100%;
  }
  .brand {
    position: absolute;
    left: 0;
    width: 340px;
    top: 92px;
    display: flex;
    flex-direction: column;
    align-items: center;
    gap: 12px;
  }
  .brand-mark {
    width: 14px;
    height: 14px;
    border-radius: 50%;
    background: var(--accent-orange);
  }
  .brand-name {
    color: var(--text-white);
    font-weight: 700;
    font-size: 21px;
    letter-spacing: -0.2px;
    white-space: nowrap;
  }
  .back-accent {
    position: absolute;
    left: 270px;
    top: 120px;
    width: 130px;
    height: 126px;
    border-radius: 50%;
    background: radial-gradient(circle at 55% 55%, var(--accent-soft) 0%, var(--accent-soft) 30%, var(--card-back) 72%);
  }
  .contact-block {
    position: absolute;
    left: 46px;
    top: 63px;
    width: 215px;
    color: var(--text-white);
  }
  .rule {
    height: 1px;
    background: var(--rule-grey);
  }
  .rule-top { width: 202px; }
  .rule-bottom { width: 195px; margin-top: 8px; }
  .person-name {
    font-weight: 500;
    font-size: 28px;
    line-height: 1;
    margin-top: 12px;
    margin-left: 2px;
    letter-spacing: 0.3px;
    white-space: nowrap;
  }
  .contact-list {
    list-style: none;
    margin-top: 12px;
    margin-left: 2px;
    font-weight: 700;
    font-size: 16px;
    line-height: 21px;
    white-space: nowrap;
  }
</style>
</head>
<body>
<main class="canvas">

  <section class="card card-front" aria-label="Business card front">
    <svg class="card-art" viewBox="0 0 415 259" aria-hidden="true">
      <path d="M12 259 C 200 242, 372 168, 415 58 L415 259 Z" fill="var(--swoosh-light)"/>
      <path d="M12 259 C 220 248, 382 182, 415 90 L415 259 Z" fill="var(--accent-orange)"/>
    </svg>
    <div class="brand">
      <span class="brand-mark"></span>
      <span class="brand-name">Harbor Lane Realty Inc</span>
    </div>
  </section>

  <section class="card card-back" aria-label="Business card back">
    <div class="back-accent" role="img" aria-label="Faint decorative ornament area"></div>
    <div class="contact-block">
      <div class="rule rule-top"></div>
      <h1 class="person-name">Dale Morrick</h1>
      <ul class="contact-list">
        <li>555-271-6094</li>
        <li>PO Box 718269</li>
        <li>Cedar Marsh FL 32987</li>
        <li>dmorrick@mailbox.test</li>
      </ul>
      <div class="rule rule-bottom"></div>
    </div>
  </section>

</main>
</body>
</html>
```